Portfolio site - Need a basic WordPress or SquareSpace site

I need a portfolio site where I have the option to keep updating it on my own. Therefore, I'm guessing I need one that uses WordPress or SquareSpace. I just need a simple and elegant design. I'm a writer (scholarly, fiction and journalism).

Target Market(s)

Adult

Industry/Entity Type

Writer

Number of Pages Required

4 page

Font styles to use
Serif

Colors
b7a5cd
e667a6
85abd2

Requirements
Must have
• Easily updatable features. I'll have to publish links and small blurbs from time to time. And maybe the occasional image.
• Pages should be:
• Home
• Work
• Press
• Contact

```html
<!DOCTYPE html>
<html lang="en">
<head>
<meta charset="utf-8">
<title>Maren Ashcroft — Writer and Comics Scholar</title>
<link rel="stylesheet" href="https://fonts.googleapis.com/css2?family=Bodoni+Moda:opsz,wght@6..96,400;6..96,500;6..96,600&family=Libre+Baskerville&family=Montserrat:wght@400&display=swap">
<style>
  :root {
    --pink: #e667a6;
    --blue: #85abd2;
    --lilac: #b7a5cd;
    --ink: #111111;
    --nav-active: #3b3bf0;
    --nav-ink: #2a2a2a;
    --white: #ffffff;
    --rule: #c9c9c9;
  }
  * { margin: 0; padding: 0; box-sizing: border-box; }
  html, body { width: 1119px; height: 1200px; overflow: hidden; background: var(--white); }
  body { position: relative; font-family: "Bodoni Moda", "Times New Roman", serif; color: var(--ink); }

  .site-header { position: absolute; left: 0; top: 0; width: 1119px; height: 98px; background: var(--pink); }
  .brand { position: absolute; left: 121px; top: 37px; font-family: "Libre Baskerville", Georgia, serif; font-size: 16px; color: var(--ink); }
  .main-nav a { position: absolute; top: 51px; font-family: "Libre Baskerville", Georgia, serif; font-size: 12px; color: var(--nav-ink); text-decoration: none; }
  .main-nav a.is-active { color: var(--nav-active); }

  .hero { position: absolute; left: 0; top: 98px; width: 1119px; height: 679px;
    background: radial-gradient(ellipse at 70% 55%, #8a6a55 0%, #5b4638 40%, #3a2e28 75%, #2c2420 100%); }
  .hero-title { position: absolute; left: 0; width: 1119px; top: 116px; padding-left: 76px; text-align: center; font-size: 50px; line-height: 50px; letter-spacing: 10px; color: var(--blue); font-weight: 400; }
  .hero-subtitle { position: absolute; left: 0; width: 1119px; top: 178px; padding-left: 114px; text-align: center; font-size: 19px; line-height: 20px; letter-spacing: 4px; color: var(--blue); }
  .hero-tagline { position: absolute; left: 0; width: 1119px; top: 259px; padding-left: 108px; text-align: center; font-family: "Montserrat", Arial, sans-serif; font-size: 16px; line-height: 18px; color: var(--ink); }
  .btn-browse { position: absolute; left: 445px; top: 320px; width: 285px; height: 42px; background: var(--pink); border-radius: 4px; font-family: "Montserrat", Arial, sans-serif; font-size: 15px; text-align: center; line-height: 38px; color: var(--ink); }

  .feature-card { position: absolute; left: 186px; top: 694px; width: 741px; height: 348px; background: var(--white); border: 2px solid var(--blue); border-radius: 8px; }
  .feature-title { position: absolute; left: 0; top: 2px; width: 737px; text-align: center; font-size: 20px; line-height: 27px; font-weight: 600; text-transform: uppercase; padding-left: 10px; }
  .feature-meta { position: absolute; left: 14px; top: 80px; font-size: 17px; line-height: 24px; font-variant: small-caps; }
  .feature-meta .cap { font-size: 23px; }
  .feature-body { position: absolute; left: 14px; top: 110px; font-size: 15.2px; line-height: 27.2px; white-space: nowrap; }
  .btn-read { position: absolute; left: 248px; top: 281px; width: 190px; height: 46px; border-radius: 23px; background: var(--pink); box-shadow: 0 3px 4px rgba(0,0,0,0.35); text-align: center; line-height: 46px; font-size: 15px; font-weight: 500; }

  .footer-rule { position: absolute; left: 162px; top: 1057px; width: 767px; height: 10px; border: 2px solid var(--rule); }
  .footer-brand { position: absolute; left: 185px; top: 1151px; font-family: "Libre Baskerville", Georgia, serif; font-size: 13px; }
  .social-list { list-style: none; }
  .social-item { position: absolute; top: 1084px; width: 80px; margin-left: -40px; text-align: center; font-size: 11px; line-height: 12px; color: var(--ink); }
  .social-item .tile { display: block; width: 58px; height: 58px; margin: 0 auto 3px; background: var(--lilac); border-radius: 6px; }
  .copyright { position: absolute; left: 376px; top: 1180px; font-size: 10px; letter-spacing: 2.6px; color: var(--blue); }
</style>
</head>
<body>
  <header class="site-header">
    <div class="brand">Maren Ashcroft</div>
    <nav class="main-nav">
      <a class="is-active" href="#" style="left:566px">HOME</a>
      <a href="#" style="left:662px">WORK</a>
      <a href="#" style="left:763px">PRESS</a>
      <a href="#" style="left:878px">CONTACT</a>
    </nav>
  </header>

  <section class="hero" role="img" aria-label="Photo of hands typing on a laptop at a café table">
    <h1 class="hero-title">Maren Ashcroft</h1>
    <p class="hero-subtitle">writter and comics scholar</p>
    <p class="hero-tagline">JOURNALS, FACTION AND SCHOLARLY PUBLICATIONS</p>
    <div class="btn-browse">BROWSE</div>
  </section>

  <article class="feature-card">
    <h2 class="feature-title">Transport of pollutants beneath the regional solid<br>waste disposal sites in partly<br>drained clay soils</h2>
    <p class="feature-meta"><span class="cap">A</span>rticle · january 2008</p>
    <p class="feature-body">Lorem ipsum dolor sit amet, consectetur adipisicing elit, sed do eiusmod tempor incididunt ut labore et<br>dolore magna aliqua. Ut enim ad minim veniam, quis nostrud exercitation ullamco laboris nisi ut aliquip<br>ex ea commodo consequat. Duis aute irure dolor in reprehenderit in voluptate velit esse cillum dolore eu<br>fugiat nulla pariatur. Excepteur sint occaecat cupidatat non proident, sunt in culpa qui officia deserunt<br>mollit&nbsp; dolor sit amet, consectetur, adipisci velit, sed quia non numquam eius modi tempora incidunt ut<br>labore et dolore magnam aliquam quaerat voluptatem.</p>
    <div class="btn-read">Read more</div>
  </article>

  <footer>
    <div class="footer-rule"></div>
    <ul class="social-list">
      <li class="social-item" style="left:404px"><span class="tile"></span>Plaza</li>
      <li class="social-item" style="left:483px"><span class="tile"></span>Lensbox</li>
      <li class="social-item" style="left:566px"><span class="tile"></span>Workhub</li>
      <li class="social-item" style="left:653px"><span class="tile"></span>Circles</li>
      <li class="social-item" style="left:743px"><span class="tile"></span>Reelcast</li>
      <li class="social-item" style="left:832px"><span class="tile"></span>Chirper</li>
    </ul>
    <div class="footer-brand">Maren Ashcroft</div>
    <p class="copyright">copyright 2018 Maren Ashcroft. All right Reserved</p>
  </footer>
</body>
</html>
```